New homepage design www.marblequill.nl

We need a new website design to go with our new designed logo.
We are a relativly small basketballclub that would like a shiny new webdesign for our homepage. We want te be able to create a real homepage/base for our clubmembers, where they can find news, upcoming events (agenda/calendar) and the related info on playing basketball at our club (games/tasks/teams and all).

The current website is located at: www.marblequill.nl but is an outdated and not so appealing design.
There are no real designfeatures of the current site that have to be transferred to the new site.
Coding in HTML/CSS/JS/JPEG/PNG is enough, making a dynamic website will be my task. I just need the design in HTML (preferrably HTML 5)

There is not a huge budget, we are a club without a main sponsor.

Feel free to be creative and amaze us!

Text for the page in the new design will be created by us, you may use some sample text for filling.

Currently used pictures in the site don't have to be transferred to the new page (preferrably not!)

Reason: For Newyear/holiday reasons

Tomorrow we will pick a design.

• The new logo as uploaded and attached.
News page.
Agenda page
HTML compatible same look and feel in all modern browsers (IE, FireFox, Chrome, Safari)
• HTML 5 validated and approved

```html
<!DOCTYPE html>
<html lang="en">
<head>
<meta charset="utf-8">
<title>Marblequill Basketball Club</title>
<link href="https://fonts.googleapis.com/css2?family=Open+Sans:wght@400;600;700&display=swap" rel="stylesheet">
<style>
:root{
  --night:#06121c;
  --navy:#213247;
  --navy-deep:#1a2d44;
  --orange:#f28a1f;
  --orange-text:#c86a12;
  --gold:#f2a541;
  --link-blue:#7fb6e6;
  --panel:#2e2e2e;
  --sidebar:#efefef;
  --rule:#dcdcdc;
  --ink:#1f3145;
  --body:#555;
  --white:#fff;
}
*{margin:0;padding:0;box-sizing:border-box}
html,body{width:952px;height:1200px;overflow:hidden}
body{position:relative;background:var(--navy);font-family:"Open Sans",Arial,sans-serif;color:var(--body)}
.top-band{position:absolute;left:0;top:0;width:952px;height:144px;background:var(--night)}
.page{position:absolute;left:79px;top:17px;width:795px;height:1107px;background:var(--white)}
.abs{position:absolute}

.brand{left:8px;top:24px;display:flex;align-items:center;gap:6px}
.brand-mark{width:40px;height:40px;border-radius:50%;background:var(--navy-deep)}
.brand-name{font-weight:700;font-size:13px;color:var(--navy-deep);letter-spacing:.3px}

.account{left:514px;top:36px;font-size:11.5px;color:#444}
.account .sep{color:#aaa;margin:0 6px}
.account .login{color:var(--orange-text)}
.search{left:636px;top:32px;width:151px;height:24px;border:1px solid #ccc;font-size:11px;color:#555;padding:4px 10px}
.search svg{position:absolute;right:7px;top:5px}

.nav{left:368px;top:81px;display:flex;align-items:center;font-size:12px;color:#444}
.nav a{text-decoration:none;color:#444;margin-left:24px}
.nav a.active{margin-left:0;background:var(--orange);color:var(--white);padding:3px 8px;border-radius:2px}

.hero{left:7px;top:135px;width:781px;height:329px;background:linear-gradient(120deg,#6b5448 0%,#3a3a48 45%,#2c3a66 80%,#4a3a40 100%)}
.hero-caption{left:508px;top:34px;width:239px;height:261px;background:rgba(0,0,0,.72);border-radius:3px;padding:16px 18px;color:#ddd}
.hero-caption h2{font-size:15px;font-weight:600;color:var(--gold);line-height:20px}
.hero-caption time{display:block;font-size:10.5px;color:var(--white);margin:8px 0 12px}
.hero-caption p{font-size:10.5px;line-height:20px}
.dots{position:absolute;left:84px;top:212px;display:flex;gap:8px}
.dots span{width:11px;height:11px;border-radius:50%;background:#888;border:1px solid #555}

.welcome{left:9px;top:484px;width:558px}
.welcome h1{font-size:21px;font-weight:400;color:var(--ink)}
.welcome h3{font-size:12.5px;font-weight:400;color:#111;margin-top:10px}
.welcome p{font-size:10.5px;line-height:18px;margin-top:3px}

.section-title{position:absolute;left:7px;font-size:20px;line-height:28px;font-weight:400;color:var(--ink)}
.more-btn{position:absolute;left:540px;width:23px;height:16px;background:var(--navy-deep);display:flex;align-items:center;justify-content:center;z-index:2}
.item{width:556px;height:144px;background:var(--panel);padding:16px 13px}
.item-photo{position:absolute;left:13px;top:16px;width:165px;height:114px}
.item-body{position:absolute;left:194px;top:13px;width:350px}
.item-body h4{font-size:13.5px;font-weight:400;color:var(--gold)}
.item-body time{display:block;font-size:10.5px;color:var(--link-blue);margin:3px 0 12px}
.item-body p{font-size:10.5px;line-height:18px;color:#ccc}

.sidebar{left:585px;top:477px;width:203px;height:520px;background:var(--sidebar);border:1px solid var(--rule);padding:10px 7px}
.sidebar h2{font-size:20px;font-weight:400;color:var(--orange-text);margin-left:1px}
.sidebar-photo{width:190px;height:111px;margin-top:4px;background:linear-gradient(160deg,#2d4f8a,#1b2e58 60%,#8a5a3a)}
.sidebar p{font-size:10.5px;line-height:18.2px;padding:0 2px 0 8px;margin-top:12px;color:#555}
.sidebar p + p{margin-top:8px}

.divider{left:7px;top:1023px;width:781px;height:1px;background:var(--rule)}
.teams-title{left:0;top:1034px;width:795px;text-align:center;font-size:12.5px;color:#111}
.sponsors{left:56px;top:1064px;width:690px;display:flex;justify-content:space-between;align-items:center;font-size:14px;font-weight:700;color:#222}
.sponsors span{display:flex;align-items:center;gap:4px}
.sponsors i{display:inline-block;width:14px;height:14px;background:#222}

.footer-links{left:79px;top:1142px;font-size:11px;color:#e6e6e6}
.footer-links .sep{color:#8a99aa;margin:0 9px}
.copyright{left:79px;top:1167px;font-size:11px;color:#e6e6e6}
.social{left:830px;top:1153px;display:flex;gap:4px}
.social span{width:20px;height:20px;border-radius:3px}
</style>
</head>
<body>
<div class="top-band"></div>

<div class="page">
  <div class="abs brand"><span class="brand-mark"></span><span class="brand-name">MARBLEQUILL</span></div>

  <div class="abs account">REGISTER<span class="sep">/</span><span class="login">LOGIN</span></div>
  <div class="abs search">Search
    <svg width="13" height="13" viewBox="0 0 13 13"><circle cx="5" cy="5" r="3.6" fill="none" stroke="#222" stroke-width="1.8"/><line x1="7.6" y1="7.6" x2="12" y2="12" stroke="#222" stroke-width="2.4"/></svg>
  </div>

  <nav class="abs nav">
    <a class="active" href="#">HOME</a><a href="#">TEAMS</a><a href="#">ABOUT</a><a href="#">GALLERY</a><a href="#">CONTACT US</a><a href="#">LINKS</a>
  </nav>

  <div class="abs hero" role="img" aria-label="Basketball dropping through a hoop in front of a blurred crowd">
    <div class="abs hero-caption">
      <h2>Nullam nec vestibulum enim venenatis neque nisl</h2>
      <time>December 23, 2013</time>
      <p>Pellentesque nec ligula dictum sapien commodo iaculis. Cras a eros eu neque aliquet fermentum in non tellus. Phasel lus aliquam, leo sit amet eleifend pulvinar, dolor nunc aliquet felis, ut lacinia leo tellus nec velit.</p>
      <div class="dots"><span></span><span></span><span></span><span></span></div>
    </div>
  </div>

  <section class="abs welcome">
    <h1>Welcome to Marblequill</h1>
    <h3>The Board of BC Marble Quill welcome you to our site.</h3>
    <p>THANKS! Thank you all very much for the nice evening party!!! The cozy familiar atmosphere inside Marble Quill has been present throughout the evening. Super!! Thank you all for coming, nice memories and fun! A special thanks to the organization of large Marble Quill game. This was great!! Thank you!</p>
  </section>

  <h2 class="section-title" style="top:615px">Latest News</h2>
  <div class="more-btn" style="top:625px"><svg width="11" height="9" viewBox="0 0 11 9"><path d="M1 1l3.5 3.5L1 8M5.5 1L9 4.5 5.5 8" fill="none" stroke="#fff" stroke-width="1.6"/></svg></div>
  <article class="abs item" style="left:7px;top:650px">
    <div class="item-photo" role="img" aria-label="Basketball resting on a wooden court floor" style="background:linear-gradient(135deg,#c9872e,#e0a33f 50%,#b9652a)"></div>
    <div class="item-body">
      <h4>Etiam congue viverra velit, non aliquet nisl venenatis</h4>
      <time>December 23, 2013</time>
      <p>Cum sociis natoque penatibus et magnis dis parturient montes, nascetur ridiculus mus. Vestibulum ante ipsum primis in faucibus orci luctus et ultrices posuere cubilia Curae; Integer blandit fermentum diam vel sagittis</p>
    </div>
  </article>

  <h2 class="section-title" style="top:819px">Upcoming Events</h2>
  <div class="more-btn" style="top:829px"><svg width="11" height="9" viewBox="0 0 11 9"><path d="M1 1l3.5 3.5L1 8M5.5 1L9 4.5 5.5 8" fill="none" stroke="#fff" stroke-width="1.6"/></svg></div>
  <article class="abs item" style="left:7px;top:854px">
    <div class="item-photo" role="img" aria-label="Referee holding a basketball" style="background:linear-gradient(90deg,#2a2a2a,#6a6a6a 30%,#2a4a9a 70%,#1f3a80)"></div>
    <div class="item-body">
      <h4>Etiam congue viverra velit, non aliquet nisl venenatis</h4>
      <time>December 23, 2013</time>
      <p>Cum sociis natoque penatibus et magnis dis parturient montes, nascetur ridiculus mus. Vestibulum ante ipsum primis in faucibus orci luctus et ultrices posuere cubilia Curae; Integer blandit fermentum diam vel sagittis</p>
    </div>
  </article>

  <aside class="abs sidebar">
    <h2>About Team</h2>
    <div class="sidebar-photo" role="img" aria-label="Team hands reaching together around a basketball"></div>
    <p>Praesent purus sem, pulvinar eget posuere in, convallis a mi. Sed massa lectus, vehicula vitae ves-tibulum nec, ultricies ut turpis. Interdum et malesuada fames ac ante ipsum primis in faucibus. Aenean elementum bibendum nulla eu varius.</p>
    <p>Duis justo nibh, blandit id laoreet aliquam, elementum et nunc. Donec mattis ornare arcu, nec porta massa sagittis ac. Praesent bibendum justo tempor adipiscing lacinia. Sed blandit dui at lectus condimentum, sit amet condimen-tum tellus semper. Vestibulum ante ipsum primis in faucibus orci luctus et ultrices posuere cubilia</p>
  </aside>

  <div class="abs divider"></div>
  <div class="abs teams-title">Teams</div>
  <div class="abs sponsors">
    <span>Ironvale</span>
    <span>Corvena</span>
    <span>Brightkit</span>
    <span>Tidewave</span>
    <span><i></i>Northgate Systems</span>
    <span>Orbwell Care</span>
  </div>
</div>

<div class="abs footer-links">Home<span class="sep">|</span>Teams<span class="sep">|</span>About<span class="sep">|</span>Gallery<span class="sep">|</span>Contact us<span class="sep">|</span>Links</div>
<div class="abs copyright">Copyright &copy; 2013 &nbsp;Marblequill. &nbsp;All rights reserved</div>
<div class="abs social">
  <span style="background:#3b5a9a" role="img" aria-label="Friendnet"></span>
  <span style="background:#3fa9e0" role="img" aria-label="Chirpline"></span>
</div>
</body>
</html>
```